Awsome new website

We are a Fencing Contracting company in Melbourne Australia. We supply and install Timer and Steel boundary fences as well as Pool fencing (e.g. glass, tubular steel). We also manufacture and install swing and sliding gates.

We want a new website that is a modern business website.
We are targeting domestic and business clients.
The design should compliment our logo and company name.
The website needs to be easy to update.

Some specifics we want.
Menu - Main menu at top of page and smaller footer menu (to add different menu items)
Slider - Main page to have a slider on it that's easy for us to add and remove slides.
Call to action - all pages to have a "call to action" logo or icon that attracts attention (see file "call_to_action.pdf)
Instant quote - we have a online quote page we need a distinctive logo or icon to redirect to this page.
Main page to have a product /Service guide (see file "website_idea.jpg")
Main page to have widgets or quick link to
o why choose us
o Brochures
o Gallery

Have a Gallery page formatted with different category galleries. e.g. Timber, Glass, Feature
Maintain the current link to our staff page with password, (link in footer menu)

Hopefully that covers everything.
Our current website is www.tallowcreekrails.com.au to have a look at the current site.
regards Doug

• Turn off blogging as we don’t want 100’s of comments from spammers to delete

We would like to implement the QX-Portal plugin (see "http://qx-portal-demo.net/" ), but this can be done after the new Theme has been implemented.

```html
<!DOCTYPE html>
<html lang="en">
<head>
<meta charset="utf-8">
<title>Tallow Creek Rails – Home</title>
<link rel="stylesheet" href="https://fonts.googleapis.com/css2?family=Montserrat:wght@400;700;800&family=Mulish:wght@400;600&display=swap">
<style>
:root{
  --red:#8c1016;
  --red-dark:#6a0a0e;
  --ink:#1c1c1c;
  --body:#333;
  --muted:#5c5c5c;
  --band:#ececec;
  --card:#f6f6f6;
  --line:#d9d9d9;
  --orange:#f56a10;
}
*{box-sizing:border-box;margin:0;padding:0}
html,body{width:1200px;height:1200px;overflow:hidden;background:#fff}
body{position:relative;font-family:"Mulish",sans-serif;color:var(--body)}
.abs{position:absolute}

/* header */
.site-header{left:0;top:0;width:1200px;height:104px;border-bottom:1px solid #e6e6e6;box-shadow:0 2px 6px rgba(0,0,0,.05)}
.brand{left:202px;top:16px;width:222px;height:72px;border:3px solid var(--red);display:flex;align-items:center;gap:8px;padding-left:12px;background:#fff}
.brand-mark{width:16px;height:16px;background:var(--red)}
.brand-name{font-family:"Montserrat",sans-serif;font-weight:800;font-size:19px;color:var(--red);line-height:1.05}
.quote-btn{left:640px;top:12px;width:154px;height:36px;border:1px solid #ccc;border-radius:3px;background:linear-gradient(#fafafa,#e5e5e5);display:flex;align-items:center;gap:8px;padding-left:6px;font-family:"Montserrat",sans-serif;font-size:9.5px;color:#9a9a9a;letter-spacing:.3px}
.quote-btn .ico{width:24px;height:24px;background:var(--red);border-radius:2px;display:grid;place-items:center}
.phone{left:822px;top:16px;display:flex;align-items:center;gap:10px;font-family:"Montserrat",sans-serif;font-weight:700;font-size:22px;color:var(--ink)}
.nav-rule{left:432px;top:62px;width:586px;height:1px;background:#eee}
.main-nav{left:493px;top:71px;display:flex;gap:22px;font-size:14px;color:#222}

/* hero */
.hero-band{left:0;top:136px;width:1200px;height:312px;background:linear-gradient(#f6f6f6,#e6e6e6)}
.hero-photo{left:590px;top:138px;width:410px;height:284px;background:linear-gradient(120deg,#c9bfae 0%,#a58c74 35%,#7b5a44 55%,#6f8a4c 85%,#85985e 100%)}
.hero-copy{left:228px;top:188px}
.hero-kicker{font-family:"Montserrat",sans-serif;font-size:21px;color:#555}
.hero-title{font-family:"Montserrat",sans-serif;font-size:37px;line-height:40px;letter-spacing:-1.5px;color:#111;font-weight:400}
.hero-title span{display:block;color:var(--red)}
.hero-lede{margin-top:6px;font-size:12.5px;line-height:15px;color:#666;width:320px}
.hero-cta{left:230px;top:343px;width:156px;height:34px;border-radius:3px;background:linear-gradient(#444,#111);color:#fff;font-family:"Montserrat",sans-serif;font-weight:700;font-size:18px;letter-spacing:-.5px;display:grid;place-items:center}

/* feature cards */
.card{top:430px;width:248px;height:228px;background:var(--card);border:1px solid #d6d6d6;border-radius:8px;text-align:center;box-shadow:0 10px 10px -6px rgba(0,0,0,.15)}
.card-left{left:200px}
.card-right{left:752px}
.card h2{font-family:"Montserrat",sans-serif;font-weight:800;font-size:18px;color:#666;margin-top:12px;letter-spacing:-.5px}
.card .thumb{width:188px;height:76px;margin:8px auto 0;border:2px solid var(--red)}
.card p{font-size:10px;line-height:12.4px;color:#444;padding:0 8px;margin-top:8px}
.view-btn{width:78px;height:24px;margin:7px auto 0;border:1px solid #ccc;border-radius:3px;background:linear-gradient(#fff,#e3e3e3);display:flex;align-items:center;justify-content:center;gap:14px;font-family:"Montserrat",sans-serif;font-weight:700;font-size:11px;color:#333}
.view-btn i{width:15px;height:15px;border-radius:50%;border:1px solid #aaa;background:#eee;display:grid;place-items:center}
.card-feature{left:446px;top:402px;width:308px;height:278px;border-radius:8px;background:linear-gradient(var(--red),var(--red-dark));text-align:center;color:#fff;box-shadow:0 2px 6px rgba(0,0,0,.3)}
.card-feature h2{font-family:"Montserrat",sans-serif;font-weight:800;font-size:23px;margin-top:14px;letter-spacing:-.5px}
.card-feature .thumb{width:222px;height:60px;margin:8px auto 0;border:2px solid #fff;background:linear-gradient(110deg,#d9bf95,#b8966a)}
.card-feature p{font-size:10px;line-height:12.4px;padding:0 32px;margin-top:10px}
.download-btn{width:164px;height:44px;margin:8px auto 0;border-radius:3px;background:linear-gradient(#ff9a35,var(--orange));display:flex;align-items:center;font-family:"Montserrat",sans-serif;font-weight:800;font-size:15px;color:#fff;overflow:hidden}
.download-btn .ico{width:42px;height:100%;background:linear-gradient(#eee,#c9c9c9);display:grid;place-items:center;margin-right:8px}

/* about */
.content-band{left:0;top:696px;width:1200px;height:364px;background:linear-gradient(#f7f7f7,#fbfbfb)}
.section{left:200px;width:800px;text-align:center}
.section h2{font-family:"Montserrat",sans-serif;font-weight:800;color:var(--red);letter-spacing:-.5px}
.section p{font-size:10px;line-height:12.4px;color:#222}
.about{top:716px}
.about h2{font-size:25px;margin-bottom:8px}
.about p+p{margin-top:12px}
.divider{left:0;top:859px;width:1200px;border-top:1px dotted #bbb}
.quality{top:880px}
.quality h2{font-size:24px;margin-bottom:8px}
.quality ul{list-style:none;margin-top:14px;font-size:10px;line-height:15.3px;color:#222}

/* footer */
.footer-rule{left:0;top:1089px;width:1200px;height:1px;background:#e2e2e2}
.footer-brand{left:198px;top:1110px;width:160px;height:52px;border:3px solid #555;display:flex;align-items:center;gap:6px;padding-left:8px}
.footer-brand .brand-mark{width:12px;height:12px;background:#555}
.footer-brand .brand-name{font-size:14px;color:#555}
.foot-title{font-family:"Montserrat",sans-serif;font-size:22px;letter-spacing:-1px;color:var(--red)}
.links{left:381px;top:1108px}
.footer-nav{display:flex;font-size:10.5px;color:#222;margin-top:6px}
.footer-nav span{padding:0 7px;border-left:1px dotted #999}
.footer-nav span:first-child{border:none;padding-left:4px}
.col-rule{left:796px;top:1110px;width:1px;height:54px;background:#ddd}
.social{left:832px;top:1108px}
.social-row{display:flex;gap:18px;margin-top:6px}
.social-row i{width:14px;height:14px;border-radius:50%;background:#8a8a8a}
</style>
</head>
<body>

<header class="site-header abs">
  <div class="brand abs"><span class="brand-mark"></span><span class="brand-name">Tallow Creek<br>Rails</span></div>
  <div class="quote-btn abs">
    <span class="ico"><svg width="12" height="14" viewBox="0 0 12 14"><path d="M6 1v10M2 7l4 4 4-4" stroke="#fff" stroke-width="2" fill="none"/></svg></span>
    QUICK QUOTE FORM
  </div>
  <div class="phone abs">
    <svg width="30" height="28" viewBox="0 0 30 28"><path d="M3 9c0-4 24-4 24 0v3h-6V9H9v3H3z" fill="none" stroke="#8c1016" stroke-width="2"/><rect x="6" y="13" width="18" height="13" rx="2" fill="none" stroke="#8c1016" stroke-width="2"/><g fill="#8c1016"><rect x="10" y="16" width="3" height="2"/><rect x="14" y="16" width="3" height="2"/><rect x="18" y="16" width="3" height="2"/><rect x="10" y="20" width="3" height="2"/><rect x="14" y="20" width="3" height="2"/><rect x="18" y="20" width="3" height="2"/></g></svg>
    03 9000 4127
  </div>
  <div class="nav-rule abs"></div>
  <nav class="main-nav abs"><span>Home</span><span>Steelguard</span><span>Instant Quote</span><span>Gallery</span><span>Product &amp; Services</span><span>Contact</span></nav>
</header>

<section class="hero-band abs"></section>
<div class="hero-photo abs" role="img" aria-label="Fencing showroom building with display gates and steel fence panels on a lawn"></div>
<div class="hero-copy abs">
  <p class="hero-kicker">WE SUPPLY</p>
  <h1 class="hero-title">STEEL BOUNDARY<span>SLIDING GATES</span></h1>
  <p class="hero-lede">Lorem ipsum dolor sit amet, consectetuer adipiscing elit, sed diam nonummy nibh euismod</p>
</div>
<div class="hero-cta abs">LEARN MORE</div>

<article class="card card-left abs">
  <h2>WHY CHOOS US</h2>
  <div class="thumb" role="img" aria-label="Family standing in front of a white picket fence" style="background:linear-gradient(100deg,#5e7a3e,#8c6c58 50%,#e9e9e9)"></div>
  <p>We offer a 12 month workmanship warranty on our fences and will clean the site for free of any fencing debris from the fence construction upon completion of the job. We can offer this workm-anship warranty</p>
  <div class="view-btn">VIEW <i><svg width="7" height="7" viewBox="0 0 7 7"><path d="M1 3.5h5M4 1l2 2.5L4 6" stroke="#777" fill="none"/></svg></i></div>
</article>

<article class="card card-right abs">
  <h2>GALLERY</h2>
  <div class="thumb" role="img" aria-label="Timber slat gate with steel frame" style="background:linear-gradient(90deg,#8a6430,#c79a55 45%,#b48442 80%,#8f9c6a)"></div>
  <p>Please feel free to look through our gallery, these are jobs that we have personally done! Please feel free to look through our gallery, these are jobs that we have personally done! jobs that we have personally done!</p>
  <div class="view-btn">VIEW <i><svg width="7" height="7" viewBox="0 0 7 7"><path d="M1 3.5h5M4 1l2 2.5L4 6" stroke="#777" fill="none"/></svg></i></div>
</article>

<article class="card-feature abs">
  <h2>BROCHURES</h2>
  <div class="thumb" role="img" aria-label="Close-up of a printed brochure page"></div>
  <p>No pool is complete without a beautiful Pool fence. See our range of Tubular Fencing designs Download our Steelguard Fencing Brochure and see what a fantastic addition to your home see what a fantastic addition to your home</p>
  <div class="download-btn"><span class="ico"><svg width="16" height="16" viewBox="0 0 16 16"><path d="M3 3l5 5 5-5M3 8l5 5 5-5" stroke="#8c1016" stroke-width="2.5" fill="none"/></svg></span>DOWNLOAD</div>
</article>

<div class="content-band abs"></div>
<section class="section about abs">
  <h2>ABOUT US</h2>
  <p>Thank you for visiting us at Tallow Creek Rails, my name is Doug and I am the Manager.<br>I built my first fence when I was in my early twenties and have been building fences ever since. Over the last few years we have spent the time looking for fantastic fencing contractors to join our team. Because we only accept the best we have built our business to be one of Victoria's largest fencing contractors.</p>
  <p>At Tallow Creek Rails, we believe in quality above all. The first fence we constructed was over 25 years ago and the number one thing we have learnt is that to do the job right the first time is the best insurance against costly rework.</p>
</section>
<div class="divider abs"></div>
<section class="section quality abs">
  <h2>“When quality counts, Count on us”</h2>
  <p>We offer a 12 month workmanshhttp://tallowcreekrails.com.au/images/bt-arise/aboutus.jpgip warranty on our fences and will clean the site for free of any debris from the fence construction upon completion of the job. We can offer this workmanship warranty because of our work practices, these include</p>
  <ul>
    <li>6KG of cement in each wooden fence post and 15 – 20KG of concrete for all Steel posts</li>
    <li>90mm galvanised nails in all rail's rather than industry standard of 75mm</li>
    <li>75mm galvanised nails in all plinth boards, rather than the industry standard 57mm</li>
    <li>Timber and Steel all sourced from Industry leaders, rather than the cheapest we can get</li>
    <li>Gates are all made to order, rather than off the rack. (this means it's always going to be a better fit)</li>
  </ul>
</section>

<footer>
  <div class="footer-rule abs"></div>
  <div class="footer-brand abs"><span class="brand-mark"></span><span class="brand-name">Tallow Creek<br>Rails</span></div>
  <div class="links abs">
    <h3 class="foot-title">Links</h3>
    <nav class="footer-nav"><span>Home</span><span>Steelguard</span><span>Instant Quote</span><span>Gallery</span><span>Product &amp; Services</span><span>Contact</span></nav>
  </div>
  <div class="col-rule abs"></div>
  <div class="social abs">
    <h3 class="foot-title">Social Connect</h3>
    <div class="social-row" aria-label="Social profiles"><i></i><i></i><i></i><i></i></div>
  </div>
</footer>

</body>
</html>
```